Business Card Needed for Crafter of Pottery, Jewelry and Artwork

Calling all designers in search of an artistic challenge.

I need a new business card design for my pottery, jewelry and artwork business, Woven Glass and Tide, based in Vancouver BC.

I would like a card that is bright and inviting and preferably incorporates my logo and a sample of photos of my work while having a clean fresh look. The following contact details would preferably be included on the card as well:
• Helena Pikeworth
• Designer
• Phone: 604.555.0172
• Email: Designer@WovenGlassandTide.example
• Website: www.WovenGlassandTide.example
• Blog: www.ShapingHillside.example

The logo is attached in two color schemes in both Vector and Source formats. On past cards I’ve also included photos of my work. By including photos of the work the pieces are showcased and it catches people’s eye and prompts them to pick up the card and look at it more closely. For example, if I leave a stack in a coffee shop I want people to be drawn to the card, to pick it up and get a sense of the my product lines. Please feel free to pull photos of my work directly off of my website. If you need photos with higher pixels please let me know and I’ll email them directly to you. The website background is bffbda (191, 251, 218). I would like the business cards to match the feel of the website for consistency but the cards do not need to use the exact same colors. My website and current business card are predominantly turquoise shades. The background uses stripes provided by the website template. I don’t know the exact colors of the stripes.

My current business card is attached to show the use of photos in a design. Please note that I am not thrilled with my own design and am looking for variations and completely new designs. This example is not meant to be used as a template or starting point.

Here is some background surrounding my company:
WGT offers one of a kind jewelry, pottery, artwork and leather bags each designed with a twist. The pottery varies from rustic every day functional ware to raku artwork. The jewelry ranges from simple sterling every day pieces to multimedia pieces incorporating stone, metal, ceramics and fabric. The artwork is multimedia, typically acrylic paired with a natural element such as bark. All the bags are leather with reworked kimono fabric or patterned silk lining.

Feel free to check out my website to get a flavour for my work and the color scheme I've used on marketing materials so far. www.wovenglassandtide.example
Updates

Thank you to everyone who has submitted a design so far. I hope everyone has received some helpful feedback.

I'm going to post a survey to customers and friends asking for their votes. If you have new designs to submit please try to get them in by Saturday March 30 at noon so that I can include it in the survey launch.

Thank you

Target Market(s)

Females aged 25-65 interested in one of a kind functional pottery and jewelry.

Industry/Entity Type

Coffee Shop

Requirements
Must have
• Contact information, website, blog
Nice to have
• Logo, photos

```html
<!DOCTYPE html>
<html lang="en">
<head>
<meta charset="utf-8">
<title>Woven Glass and Tide – Business Card</title>
<link rel="stylesheet" href="https://fonts.googleapis.com/css2?family=Cormorant+Garamond:wght@400&family=Italianno&display=swap">
<style>
  :root {
    --turquoise: #29bdc5;
    --mint: #bfe3d6;
    --paper: #ffffff;
    --ink-light: #ffffff;
    --pottery-navy: #25226a;
    --pottery-blue: #3a3fb0;
    --pottery-aqua: #5fe6f0;
  }
  * { margin: 0; padding: 0; box-sizing: border-box; }
  html, body {
    width: 1200px;
    height: 900px;
    overflow: hidden;
    background: var(--paper);
  }
  .canvas {
    position: relative;
    width: 1200px;
    height: 900px;
  }
  .card-shapes {
    position: absolute;
    inset: 0;
  }
  .card-shapes .bg { fill: var(--turquoise); }
  .card-shapes .band { fill: var(--mint); }
  .card-shapes .panel { fill: var(--paper); stroke: var(--mint); stroke-width: 7; }

  .wordmark {
    position: absolute;
    left: 258px;
    width: 685px;
    font-family: "Cormorant Garamond", "Times New Roman", serif;
    font-weight: 400;
    color: var(--ink-light);
    text-transform: uppercase;
    white-space: nowrap;
  }
  .wordmark-main {
    top: 162px;
    text-align: center;
    font-size: 66px;
    letter-spacing: 10px;
    line-height: 1;
  }
  .wordmark-sub {
    top: 262px;
    padding-left: 142px;
    font-size: 30px;
    letter-spacing: 4px;
    line-height: 1;
  }

  .contact {
    position: absolute;
    left: 285px;
    font-family: "Italianno", cursive;
    color: var(--ink-light);
    font-size: 25px;
    line-height: 30.5px;
    white-space: nowrap;
  }
  .contact-person { top: 476px; }
  .contact-details { top: 731px; }

  .work-showcase {
    position: absolute;
    left: 632px;
    top: 478px;
    width: 236px;
    height: 228px;
    border-radius: 18px;
    background: linear-gradient(160deg, var(--pottery-blue) 0%, var(--pottery-navy) 70%);
  }
</style>
</head>
<body>
<main class="canvas">
  <svg class="card-shapes" width="1200" height="900" viewBox="0 0 1200 900" aria-hidden="true">
    <!-- front face -->
    <rect class="bg" x="258" y="26" width="685" height="419"/>
    <path class="band" d="M258 432 H733 L752 416 H943 V445 H258 Z"/>
    <!-- back face -->
    <rect class="bg" x="258" y="457" width="685" height="419"/>
    <path class="panel" d="M553 457 L578 690 Q585 745 640 742 L943 712 V457 Z"/>
  </svg>

  <section class="card-front">
    <h1 class="wordmark wordmark-main">Woven Glass</h1>
    <p class="wordmark wordmark-sub">and Tide</p>
  </section>

  <section class="card-back">
    <div class="contact contact-person">
      <p class="contact-name">Helena Pikeworth</p>
      <p class="contact-role">Designer</p>
    </div>
    <div class="work-showcase" role="img" aria-label="Illustration of handmade pottery: a jeweled shield-shaped piece beside a tall vase with brushes"></div>
    <div class="contact contact-details">
      <p>Phone: 604.555.0172</p>
      <p>Email: Designer@WovenGlassandTide.example</p>
      <p>Website: www.WovenGlassandTide.example</p>
      <p>Blog: www.ShapingHillside.example</p>
    </div>
  </section>
</main>
</body>
</html>
```